Seasonal Produce Calender Design

Design a seasonal fruit and vegetable calender made ready to print in various sizes. fruits and vegetables to be categorised into moths they are in season. File provided with content. Design is to flow with current company Logo, colours and brand identity. Can provide designers with link to similar calenders.

Please see link this is what im after:

https://www.harlowbrant.com.au/wp-content/uploads/2018/07/Seasonal-Calendar-Alts.jpg

Font styles to use
Serif

Colors

Designer to choose colors to be used in the design.

```html
<!DOCTYPE html>
<html lang="en">
<head>
<meta charset="utf-8">
<title>Seasonal Fruit &amp; Vegetable Calendar</title>
<link href="https://fonts.googleapis.com/css2?family=Bebas+Neue&family=Oswald:wght@500;700&family=Open+Sans:wght@600&display=swap" rel="stylesheet">
<style>
  :root{
    --ink:#1f1f1f;
    --white:#ffffff;
    --black:#000000;
    --summer:#d3263a;
    --autumn:#f4b400;
    --winter:#6a3b1f;
    --spring:#2f7a34;
    --panel:rgba(255,255,255,0.86);
  }
  *{margin:0;padding:0;box-sizing:border-box}
  html,body{width:1200px;height:2400px;overflow:hidden;background:var(--white)}
  .poster{position:relative;width:1200px;height:2400px;overflow:hidden;font-family:"Open Sans",Arial,sans-serif;color:var(--ink)}

  .hero{position:absolute;left:0;top:0;width:1200px;height:490px;
    background:radial-gradient(circle at 25% 40%,#33406b 0 12%,transparent 22%),
               radial-gradient(circle at 78% 20%,#6cbf3a 0 10%,transparent 20%),
               radial-gradient(circle at 88% 60%,#c8151c 0 12%,transparent 22%),
               radial-gradient(circle at 50% 15%,#e8401e 0 10%,transparent 22%),
               linear-gradient(120deg,#3f7a2a,#d8461d 45%,#7a2e45 65%,#2e6a2a)}
  .brand{position:absolute;left:0;right:0;top:205px;display:flex;align-items:center;justify-content:center;gap:14px}
  .brand-dot{width:22px;height:22px;border-radius:50%;background:var(--white)}
  .brand-name{font-family:"Oswald",sans-serif;font-weight:500;color:var(--white);font-size:40px;line-height:1;letter-spacing:1px}
  .hero-title{position:absolute;left:0;right:0;top:395px;text-align:center;font-family:"Bebas Neue",sans-serif;
    font-size:112px;line-height:1;color:var(--white);letter-spacing:3px;white-space:nowrap;text-shadow:0 2px 6px rgba(0,0,0,.35)}

  .word-band{position:absolute;left:0;top:497px;width:1200px;height:170px;background:var(--black)}
  .word-art{position:absolute;left:28px;top:14px;width:1144px;height:142px;
    background:linear-gradient(90deg,#e9a21b,#c7342a 25%,#7fae2c 50%,#e86b1f 75%,#d6b21e)}

  .season{position:absolute;left:0;width:1200px;height:379px;overflow:hidden}
  .season-photo{position:absolute;inset:0}
  .summer{top:673px} .summer .season-photo{background:linear-gradient(100deg,#a3121e,#e23a3a 40%,#c81f2a 70%,#8e0d18)}
  .autumn{top:1052px} .autumn .season-photo{background:linear-gradient(100deg,#8fa52a,#f3c22c 35%,#f7d86a 60%,#e99a1c)}
  .winter{top:1431px} .winter .season-photo{background:linear-gradient(100deg,#5a4030,#a88c74 40%,#d8cbbb 65%,#7a5e46)}
  .spring{top:1810px} .spring .season-photo{background:linear-gradient(100deg,#1f5a22,#6fa83a 40%,#9cc45a 65%,#2f6e2a)}

  .season-name{position:absolute;left:26px;bottom:46px;writing-mode:vertical-rl;transform:rotate(180deg);
    font-family:"Oswald",sans-serif;font-weight:700;font-size:90px;line-height:1;color:var(--white);text-transform:uppercase;letter-spacing:-3px;white-space:nowrap}
  .season-months{position:absolute;left:124px;bottom:58px;writing-mode:vertical-rl;transform:rotate(180deg);
    font-family:"Open Sans",sans-serif;font-weight:600;font-size:16px;color:var(--white);white-space:nowrap}

  .panel{position:absolute;left:172px;top:21px;width:998px;height:340px;background:var(--panel)}
  .divider{position:absolute;top:22px;bottom:10px;width:1px}
  .divider.one{left:301px} .divider.two{left:741px}
  .heading{position:absolute;top:14px;font-family:"Oswald",sans-serif;font-weight:500;font-size:28px;line-height:1;text-transform:uppercase}
  .h-fruit{left:31px} .h-veg{left:326px} .h-herb{left:768px}
  .list{position:absolute;top:55px;list-style:none;font-size:14px;line-height:16.4px;white-space:nowrap}

  .summer .heading{color:var(--summer)} .summer .divider{background:var(--summer)}
  .autumn .heading{color:var(--autumn)} .autumn .divider{background:var(--autumn)}
  .winter .heading{color:var(--winter)} .winter .divider{background:var(--winter)}
  .spring .heading{color:var(--spring)} .spring .divider{background:var(--spring)}

  .contact-band{position:absolute;left:0;top:2188px;width:1200px;height:82px;background:var(--white);
    text-align:center;font-family:"Oswald",sans-serif;font-weight:500;font-size:28px;line-height:82px;color:var(--ink)}
  .fruit-strip{position:absolute;left:0;top:2270px;width:1200px;height:130px;
    background:linear-gradient(90deg,#e2653a,#b61e2e 10%,#9cc23a 20%,#f08a1c 30%,#d01f2a 40%,#f3c21c 50%,#7fbf3a 60%,#8a1a3a 70%,#2a3a7a 78%,#e8851c 85%,#5a2a6a 90%,#f2c31b 95%,#c81f2a)}
</style>
</head>
<body>
<div class="poster">

  <header class="hero" role="img" aria-label="Photograph of fresh fruit and vegetables: blueberries, tomatoes, carrots, apples, capsicum, asparagus and raspberries">
  </header>
  <div class="brand"><span class="brand-dot"></span><span class="brand-name">Orchard Lane Produce</span></div>
  <h1 class="hero-title">Seasonal Fruit &amp; Vegetable</h1>

  <div class="word-band">
    <div class="word-art" role="img" aria-label="The word CALENDAR formed from arrangements of fresh fruit"></div>
  </div>

  <section class="season summer">
    <div class="season-photo" role="img" aria-label="Close-up photograph of strawberries"></div>
    <h2 class="season-name">Summer</h2>
    <p class="season-months">December • January • February</p>
    <div class="panel">
      <h3 class="heading h-fruit">Fruits</h3>
      <h3 class="heading h-veg">Vegetable</h3>
      <h3 class="heading h-herb">Herbs &amp; Spices</h3>
      <span class="divider one"></span><span class="divider two"></span>
      <ul class="list" style="left:31px"><li>Apricot</li><li>Banana</li><li>Blackberries</li><li>Blueberries</li><li>Boysenberries</li><li>Cantaloupe</li><li>Cherries</li><li>Currants</li><li>Fig</li><li>Grapefruit</li><li>Grapes</li><li>Honeydew</li><li>Lemon</li><li>Loganberries</li><li>Lychee</li><li>Mango</li><li>Mulberries</li></ul>
      <ul class="list" style="left:161px"><li>Nectarine</li><li>Orange Valencia</li><li>Passionfruit</li><li>Peach</li><li>Plum</li><li>Pineapple</li><li>Rambutan</li><li>Raspberries</li><li>Rhubarb</li><li>Strawberries</li><li>Tamarillo</li><li>Watermelon</li></ul>
      <ul class="list" style="left:326px"><li>Vegetable</li><li>Asparagus</li><li>Avocado</li><li>Beans (Butter, Green)</li><li>Beetroot</li><li>Cabbage</li><li>Capsicum</li><li>Carrot</li><li>Celery</li><li>Corn</li><li>Cucumber</li><li>Daikon</li><li>Eggplant</li><li>Leek</li><li>Lettuce</li><li>Okra</li><li>Onion</li></ul>
      <ul class="list" style="left:490px"><li>Onion, Spring</li><li>Peas</li><li>Potato</li><li>Radish</li><li>Shallot</li><li>Silverbeet</li><li>Snow Peas</li><li>Squash</li><li>Sugarsnaps</li><li>Tomato</li><li>Watercress</li><li>Zucchini</li><li>Zucchini Flower</li></ul>
      <ul class="list" style="left:774px"><li>Basil</li><li>Chervil</li><li>Chilli</li><li>Chives</li><li>Coriander</li><li>Dill</li><li>Garlic</li><li>Ginger</li><li>Lime, Kaffir (Leaves)</li><li>Lemongrass</li><li>Mint</li><li>Oregano</li><li>Parsley</li><li>Rosemary</li><li>Sage</li><li>Tarragon</li><li>Thyme</li></ul>
    </div>
  </section>

  <section class="season autumn">
    <div class="season-photo" role="img" aria-label="Close-up photograph of sliced citrus, kiwi fruit and berries"></div>
    <h2 class="season-name">Autumn</h2>
    <p class="season-months">March • April • May</p>
    <div class="panel">
      <h3 class="heading h-fruit">Fruits</h3>
      <h3 class="heading h-veg">Vegetable</h3>
      <h3 class="heading h-herb">Herbs &amp; Spices</h3>
      <span class="divider one"></span><span class="divider two"></span>
      <ul class="list" style="left:31px"><li>Avocado</li><li>Blackberries</li><li>Banana</li><li>Cumquat</li><li>Custard Apple</li><li>Fig</li><li>Grapefruit</li><li>Grapes</li><li>Guava</li><li>Honeydew</li><li>Kiwi Fruit</li><li>Lemon</li><li>Lime</li><li>Mandarin Imperial</li><li>Mango</li><li>Mangosteen</li><li>Nashi</li></ul>
      <ul class="list" style="left:178px"><li>Orange(Navel,<br>Valencia)</li><li>Papaya</li><li>Passionfruit</li><li>Peach</li><li>Pear Nashi</li><li>Persimmon</li><li>Plum</li><li>Pomegranate</li><li>Prickly Pear</li><li>Quince</li><li>Rambutan</li><li>Raspberries</li><li>Rhubarb</li><li>Rockmelon</li><li>Strawberries</li><li>Tamarillo</li></ul>
      <ul class="list" style="left:326px"><li>Artichoke Jerusalem</li><li>Asian Greens (Bok<br>Choy, Choysum,<br>Gailaan, Wombok)</li><li>Avocado</li><li>Beans(Borlotti,<br>Butter, Green)</li><li>Beetroot</li><li>Bokchoy</li><li>Broccoli</li><li>Brussels Sprouts</li><li>Cabbage</li><li>Capsicum</li><li>Carrot</li><li>Cauliflower</li><li>Celery</li><li>Choko</li></ul>
      <ul class="list" style="left:490px"><li>Corn</li><li>Cucumber</li><li>Daikon</li><li>Eggplant</li><li>Fennel</li><li>Leek</li><li>Lettuce</li><li>Mushroom(Field,<br>Pine, Slippery<br>Jacks)</li><li>Okra</li><li>Onion</li><li>Onion Spring</li><li>Parsnip</li><li>Peas</li><li>Potato</li><li>Pumpkin</li></ul>
      <ul class="list" style="left:626px"><li>Radish</li><li>Shallot</li><li>Silverbeet</li><li>Spinach</li><li>Squash</li><li>Swede</li><li>Sweet Potato</li><li>Tomato</li><li>Turnip</li><li>Watercress</li><li>Witlof</li><li>Zucchini</li></ul>
      <ul class="list" style="left:768px"><li>Basil</li><li>Chervil</li><li>Chilli</li><li>Chives</li><li>Coriander</li><li>Dill</li><li>Ginger</li><li>Lime, Kaffir (Leaves)</li><li>Lemongrass</li><li>Mint</li><li>Oregano</li><li>Parsley</li><li>Rosemary</li><li>Sage</li><li>Tarragon</li><li>Thyme</li></ul>
    </div>
  </section>

  <section class="season winter">
    <div class="season-photo" role="img" aria-label="Close-up photograph of mushrooms"></div>
    <h2 class="season-name">Winter</h2>
    <p class="season-months">June • July • August</p>
    <div class="panel">
      <h3 class="heading h-fruit">Fruits</h3>
      <h3 class="heading h-veg">Vegetable</h3>
      <h3 class="heading h-herb">Herbs &amp; Spices</h3>
      <span class="divider one"></span><span class="divider two"></span>
      <ul class="list" style="left:31px"><li>Avocado</li><li>Cumquat</li><li>Custard Apple</li><li>Feijoa</li><li>Grapefruit</li><li>Kiwi Fruit</li><li>Lemon</li><li>Lime</li><li>Mandarin(Ellendale,<br>Imperial, Murcot)</li><li>Orange(Blood, Navel,<br>Seville)</li><li>Pear Nashi</li><li>Persimmon</li><li>Pineapple</li><li>Quince</li></ul>
      <ul class="list" style="left:181px"><li>Rhubarb</li><li>Tamarillo</li><li>Tangelo</li></ul>
      <ul class="list" style="left:326px"><li>Asian Greens( Bok<br>Choy, Choy Sum, Gai<br>Laan, Wombok)</li><li>Beetroot</li><li>Broccoli</li><li>Broccolini</li><li>Beans, Broad</li><li>Brussels Sprouts</li><li>Cabbage</li><li>Carrot</li><li>Cauliflower</li><li>Celeriac</li><li>Celery</li><li>Chokos</li><li>Fennel</li><li>Horseradish</li></ul>
      <ul class="list" style="left:503px"><li>Kale</li><li>Kohlrabi</li><li>Leek</li><li>Lettuce</li><li>Mushrooms</li><li>Okra</li><li>Onion</li><li>Onion, Spring</li><li>Parsnip</li><li>Peas</li><li>Peas, Snow</li><li>Potato</li><li>Pumpkin</li><li>Radish</li><li>Shallot</li><li>Silverbeet</li></ul>
      <ul class="list" style="left:625px"><li>Spinach</li><li>Swede</li><li>Sweet Potato</li><li>Turnip</li></ul>
      <ul class="list" style="left:768px"><li>Ginger</li><li>Coriander</li><li>Dill</li><li>Mint</li><li>Oregano</li><li>Parsley</li><li>Rosemary</li></ul>
    </div>
  </section>

  <section class="season spring">
    <div class="season-photo" role="img" aria-label="Close-up photograph of green vegetables: broccoli, peas and cabbage"></div>
    <h2 class="season-name">Spring</h2>
    <p class="season-months">September • October • November</p>
    <div class="panel">
      <h3 class="heading h-fruit">Fruits</h3>
      <h3 class="heading h-veg">Vegetable</h3>
      <h3 class="heading h-herb">Herbs &amp; Spices</h3>
      <span class="divider one"></span><span class="divider two"></span>
      <ul class="list" style="left:31px"><li>Asparagus</li><li>Avocado</li><li>Banana</li><li>Blueberries (Start<br>Of Nov.)</li><li>Cantaloupe</li><li>Cherry</li><li>Cumquat</li><li>Grapefruit</li><li>Honeydew</li><li>Kiwi Fruit</li><li>Lemon</li><li>Lime</li><li>Loquat</li><li>Lychee</li><li>Mandarin (Ellendale,<br>Imperial, Murcot)</li></ul>
      <ul class="list" style="left:181px"><li>Mango</li><li>Mulberries</li><li>Orange (Blood,<br>Seville,<br>Valencia)</li><li>Papaya</li><li>Pear Corella</li><li>Pepino</li><li>Pineapple</li><li>Rhubarb</li><li>Strawberries</li><li>Starfruit</li><li>Tangelo</li><li>Watermelon</li></ul>
      <ul class="list" style="left:326px"><li>Artichoke(Globe,<br>Jerusalem)</li><li>Asian Greens( Bok<br>Choy, Choy Sum, Gai<br>Laan, Wombok)</li><li>Beans(Broad, Green)</li><li>Beetroot</li><li>Broccoli</li><li>Brussels Sprouts</li><li>Cabbage</li><li>Capsicum</li><li>Carrot</li><li>Cauliflower</li><li>Celery</li><li>Choko</li><li>Corn</li></ul>
      <ul class="list" style="left:503px"><li>Cucumber</li><li>Daikon</li><li>Eggplant</li><li>Fennel</li><li>Leek</li><li>Lettuce</li><li>Mushrooms</li><li>Okra</li><li>Onion</li><li>Onion, Spring</li><li>Parsnip</li><li>Peas</li><li>Potato</li><li>Pumpkin</li><li>Radish</li><li>Shallot</li></ul>
      <ul class="list" style="left:625px"><li>Silverbeet</li><li>Spinach</li><li>Squash</li><li>Swede</li><li>Sweet Potato</li><li>Tomato</li><li>Turnip</li><li>Watercress</li><li>Witlof</li><li>Zucchini</li></ul>
      <ul class="list" style="left:768px"><li>Basil</li><li>Chervil</li><li>Chilli</li><li>Chives</li><li>Coriander</li><li>Dill</li><li>Garlic</li><li>Ginger</li><li>Lime, Kaffir (Leaves)</li><li>Lemongrass</li><li>Mint</li><li>Oregano</li><li>Parsley</li><li>Rosemary</li><li>Sage</li><li>Tarragon</li><li>Thyme</li></ul>
    </div>
  </section>

  <footer class="contact-band">ADDRESSES ... PHONES</footer>
  <div class="fruit-strip" role="img" aria-label="Strip of diagonal slices of fruit photographs: peach, cherries, grapes, orange, strawberry, mango, apple, pomegranate, avocado, blueberries, papaya, plum, kiwi fruit, banana and apple"></div>

</div>
</body>
</html>
```